Cleaning Company needs a new business card design

Hi, We are looking for new business card designs to update with our latest logo and company information.
We would like to see designs using the colours:
Royal Blue #4169E1 - this is our company colour so this has to be in there. Please feel free to experiment with other colours.
Must include:
Front of business card:
Logo
Back of the business card:
0800 529 6081
07438 915 702
Email: info@pkrtidyhomes.co.uk
Web: www.pkrtidyhomes.co.uk
Services:
End of Tenancy
Carpet & Upholstery
Regular & One Off
all work fully insured.
The front of the business card with the logo can be made to look raised print. The blue man to be a shiny finish.
The business card needs to be presented in a matt finish
The business must be in the following styles:
Standard Square with rounded corners.
Thank you to all that take part in this.
Target Market(s)
Men and Women of different ages in the UK.
Industry/Entity Type
House Cleaning
Contact Information for Business Card
Front of business card:
Logo
0800 529 6081
07438 915 702
Email: pkrtidy@mailbox-demo.co.uk
Services:
End of Tenancy
Carpet & Upholstery
Regular & One Off
all work fully insured.

```html
<!DOCTYPE html>
<html lang="en">
<head>
<meta charset="utf-8">
<title>PKR Tidy Homes – Business Card</title>
<link rel="stylesheet" href="https://fonts.googleapis.com/css2?family=Arimo:wght@400;700&family=Open+Sans:wght@400;600;700&display=swap">
<style>
  :root {
    --backdrop: #2b2b2b;
    --royal-deep: #0f5d96;
    --royal-mid: #1b7dbf;
    --frame-blue: #1c6fa9;
    --sky: #29a9e1;
    --navy: #27348b;
    --paper: #ffffff;
    --paper-shade: #f4f5f6;
    --ink-soft: #5a6a7a;
  }
  * { box-sizing: border-box; margin: 0; padding: 0; }
  html, body { width: 1200px; height: 900px; overflow: hidden; }
  body { background: var(--backdrop); position: relative; font-family: "Arimo", Arial, sans-serif; }

  .card { position: absolute; left: 240px; width: 720px; height: 410px; border-radius: 26px; }

  /* Front */
  .card-front { top: 25px; background: var(--paper); padding: 12px; }
  .front-panel {
    width: 100%; height: 100%; border-radius: 18px;
    background: radial-gradient(ellipse at 40% 40%, var(--royal-mid), var(--royal-deep) 80%);
    display: flex; flex-direction: column; align-items: center; justify-content: center; gap: 26px;
  }
  .front-brand { display: flex; align-items: center; gap: 16px; }
  .brand-dot { width: 30px; height: 30px; border-radius: 50%; background: var(--paper); }
  .front-brand .brand-name { font-family: "Open Sans", Arial, sans-serif; font-weight: 600; font-size: 46px; color: var(--paper); }
  .front-web { display: flex; align-items: center; gap: 14px; color: var(--paper); font-size: 17px; letter-spacing: 0.3px; }
  .front-web .rule { width: 70px; height: 1px; background: var(--paper); opacity: 0.8; }

  /* Back */
  .card-back { top: 465px; background: var(--frame-blue); padding: 12px; }
  .back-panel {
    position: relative; width: 100%; height: 100%; border-radius: 18px; overflow: hidden;
    background: linear-gradient(180deg, var(--paper), var(--paper-shade));
  }
  .back-brand { position: absolute; top: 26px; right: 34px; display: flex; align-items: center; gap: 10px; }
  .back-brand .brand-dot { width: 18px; height: 18px; background: var(--navy); }
  .back-brand .brand-name { font-family: "Open Sans", Arial, sans-serif; font-weight: 700; font-size: 22px; color: var(--navy); }

  .divider { position: absolute; top: 108px; height: 2px; }
  .divider-long { left: 0; width: 540px; background: var(--sky); }
  .divider-short { left: 552px; width: 130px; background: var(--navy); }

  .holder { position: absolute; left: 40px; top: 150px; width: 240px; }
  .holder-name { font-family: "Open Sans", Arial, sans-serif; font-weight: 700; font-size: 18px; color: var(--sky); }
  .holder-title { font-size: 13px; color: var(--navy); margin-top: 2px; padding-bottom: 6px; border-bottom: 2px solid var(--sky); }

  .contacts { position: absolute; left: 40px; top: 222px; list-style: none; display: flex; flex-direction: column; gap: 9px; }
  .contacts li { display: flex; align-items: center; gap: 12px; font-size: 15px; color: var(--sky); }
  .contacts svg { width: 16px; height: 16px; flex: none; }

  .services-band {
    position: absolute; left: 0; right: 0; bottom: 0; height: 62px; background: var(--sky);
    display: flex; align-items: center; justify-content: space-between; padding: 0 18px;
  }
  .band-figure { width: 30px; height: 36px; border-radius: 6px; background: rgba(255,255,255,0.55); }
  .services { list-style: none; display: flex; gap: 22px; }
  .services li { display: flex; align-items: center; gap: 6px; color: var(--paper); font-size: 16px; }
  .services svg { width: 18px; height: 14px; }
</style>
</head>
<body>
  <section class="card card-front" aria-label="Card front">
    <div class="front-panel">
      <div class="front-brand">
        <span class="brand-dot"></span>
        <span class="brand-name">PKR Tidy Homes Limited</span>
      </div>
      <div class="front-web">
        <span class="rule"></span>
        <span>www.pkrtidyhomes.co.uk</span>
        <span class="rule"></span>
      </div>
    </div>
  </section>

  <section class="card card-back" aria-label="Card back">
    <div class="back-panel">
      <div class="back-brand">
        <span class="brand-dot"></span>
        <span class="brand-name">PKR Tidy Homes Limited</span>
      </div>
      <span class="divider divider-long"></span>
      <span class="divider divider-short"></span>

      <div class="holder">
        <p class="holder-name">YOUR NAME</p>
        <p class="holder-title">Title</p>
      </div>

      <ul class="contacts">
        <li>
          <svg viewBox="0 0 16 16" fill="none" stroke="#27348b" stroke-width="1.4"><circle cx="8" cy="8" r="7"/><path d="M5.5 4.5l1.3 1.8-.8 1c.5 1 1.3 1.8 2.3 2.3l1-.8 1.8 1.3-.9 1.2C7.4 11 5 8.6 4.3 5.4z" fill="#27348b" stroke="none"/></svg>
          <span>0800 529 6081</span>
        </li>
        <li>
          <svg viewBox="0 0 16 16" fill="none" stroke="#27348b" stroke-width="1.4"><rect x="4" y="1" width="8" height="14" rx="1.5"/><line x1="7" y1="12.5" x2="9" y2="12.5"/></svg>
          <span>07438 915 702</span>
        </li>
        <li>
          <svg viewBox="0 0 16 16" fill="none" stroke="#27348b" stroke-width="1.3"><rect x="1" y="3.5" width="14" height="9"/><path d="M1 3.5l7 5 7-5"/></svg>
          <span>pkrtidy@mailbox-demo.co.uk</span>
        </li>
      </ul>

      <div class="services-band">
        <span class="band-figure" role="img" aria-label="Small figure of a person vacuuming"></span>
        <ul class="services">
          <li><svg viewBox="0 0 18 14"><path d="M1 7l5 5L17 1" fill="none" stroke="#fff" stroke-width="3"/></svg>End of Tenancy</li>
          <li><svg viewBox="0 0 18 14"><path d="M1 7l5 5L17 1" fill="none" stroke="#fff" stroke-width="3"/></svg>Carpet &amp; Upholstery</li>
          <li><svg viewBox="0 0 18 14"><path d="M1 7l5 5L17 1" fill="none" stroke="#fff" stroke-width="3"/></svg>Regular &amp; One Off</li>
          <li><svg viewBox="0 0 18 14"><path d="M1 7l5 5L17 1" fill="none" stroke="#fff" stroke-width="3"/></svg>all work fully insured</li>
        </ul>
        <span class="band-figure" role="img" aria-label="Small figure of a person vacuuming"></span>
      </div>
    </div>
  </section>
</body>
</html>
```